Business Card Design for Vintage Jazz

I am a vintage jazz band leader in New York City. My groups play the music of the 1920s, 1930s and 1940s. My website is marlowpeskin.com for more info on what I do.

I am looking for a two sided business card design that has the look and feel of a really nice business card from the 1930s. I need to convey with the design that my work has that vintage kind of class and style, but also conveys that we are fun and entertaining.

Most importantly it should make a bold staement. If Hollis Varnum had a card, what would it have looked like? I want a card that I feel confident will make an impact and will let people know that my work is te the top that NYC has to offer in vintage jazz..

Note that I have only decided to avoid the "committed payment" option as I have not used this service before. Assuming that I get quality work I will select a design from those presented.

Target Market(s)

people who want to hire my band for events, media, and new fans of the band

Industry/Entity Type

Performing Art

Contact Information for Business Card

Definitely a matte finish, possibly a sort of old style of paper with that brown tint? definitely a thick card.

Requirements
Must have
• FRONT
• My name: Marlow Peskin
• What I do: Bandleader, Guitarist, Vocalist, Songwriter
• Contact Details: marlowpeskin.com marlow@marlowpeskin.com 646-555-0187
• BACK
• My Social Media Links:
• facebook.marlowpeskin.com
• twitter, instagram, linkedin: marlowpeskin
• I'm also including a photo image I would like to use. The photo's background is not needed, and to be honest isn't really desireable. Just looking to use the image of me.
Nice to have
• I'm attaching which could be used as is, omitted from the card, or altered maybe with text going around the outside of the circle or in some other way. It may need some clean up to the edges of the lettering as we only use it for the website thumbnail.
• If there's space I'd like to include the text "join our mailing list for a free song download: freesong.marlowpeskin.com" If not perhaps just "Download a Free Song at: freesong.marlowpeskin.com - something to this end.
Should not have
• anything cartoony. Don't think retro 90s's vision of the swing era, think actual swing era!
• anything modern. Got to look old school
• Try to avoid dark backgrounds. Since we often play in bars and clubs where it is dar, a d
• avoid script fonts.

```html
<!DOCTYPE html>
<html lang="en">
<head>
<meta charset="utf-8">
<title>Marlow Peskin — Business Card</title>
<link rel="stylesheet" href="https://fonts.googleapis.com/css2?family=Oswald:wght@500;700&family=Domine:wght@400&display=swap">
<style>
  :root {
    --page: #ffffff;
    --paper-light: #ebe5a6;
    --paper-mid: #d9d99a;
    --paper-edge: #a8bf8e;
    --maroon: #3d1616;
    --maroon-deep: #2c0f0f;
    --ink: #3a2a22;
    --ribbon: #eeebd8;
    --ribbon-fold: #c9c6b0;
    --banner: #ffffff;
    --banner-ink: #111111;
    --photo-light: #d8d8d0;
    --photo-dark: #3c3c3a;
  }
  * { box-sizing: border-box; margin: 0; padding: 0; }
  html, body {
    width: 1200px; height: 848px; overflow: hidden;
    background: var(--page);
  }
  .canvas { position: relative; width: 1200px; height: 848px; }

  .card {
    position: absolute; top: 129px;
    width: 341px; height: 580px; overflow: hidden;
    background: radial-gradient(ellipse 62% 58% at 50% 50%, var(--paper-light) 0%, var(--paper-mid) 62%, var(--paper-edge) 100%);
  }
  .card--front { left: 256px; }
  .card--back { left: 609px; }

  /* Front */
  .monogram-seal {
    position: absolute; left: 93px; top: 11px;
    width: 156px; height: 156px; border-radius: 50%;
    background: var(--maroon);
  }
  .name-heading {
    position: absolute; left: 0; right: 0; top: 198px;
    text-align: center;
    font-family: "Oswald", sans-serif; font-weight: 700;
    font-size: 38px; letter-spacing: 0.5px; line-height: 1;
    color: var(--maroon);
    text-transform: uppercase;
  }
  .roles { position: absolute; left: 0; top: 0; width: 341px; height: 520px; list-style: none; }
  .role {
    position: absolute; left: 62px; width: 218px; height: 34px;
    transform: rotate(-4deg);
  }
  .role__band {
    position: absolute; inset: 0;
    background: var(--ribbon);
    clip-path: polygon(0 0, 100% 0, 93% 50%, 100% 100%, 0 100%, 5% 50%);
  }
  .role__fold {
    position: absolute; left: 8px; top: 24px; width: 60px; height: 16px;
    background: var(--ribbon-fold);
    transform: skewX(-30deg);
    z-index: -1;
  }
  .role__label {
    position: relative; display: block;
    text-align: center; line-height: 34px;
    font-family: "Domine", serif; font-size: 16px; color: var(--ink);
  }
  .role:nth-child(1) { top: 279px; }
  .role:nth-child(2) { top: 338px; }
  .role:nth-child(3) { top: 393px; }
  .role:nth-child(4) { top: 446px; }

  .contact-bar {
    position: absolute; left: 0; right: 0; bottom: 0; height: 60px;
    background: var(--maroon-deep);
    display: flex; flex-direction: column; justify-content: center; align-items: center;
    font-family: "Oswald", sans-serif; font-weight: 500;
    font-size: 13px; line-height: 17px; color: #ffffff; letter-spacing: 0.2px;
  }

  /* Back */
  .social-banner {
    position: absolute; height: 46px;
    background: var(--banner);
    display: flex; align-items: center; gap: 12px;
    font-family: "Oswald", sans-serif; font-weight: 500; font-size: 16px;
    color: var(--banner-ink); letter-spacing: 0.3px;
    box-shadow: 0 4px 6px rgba(0,0,0,0.25);
  }
  .social-banner--site {
    left: 0; top: 26px; width: 236px; padding-left: 16px;
    clip-path: polygon(0 0, 100% 0, 90% 100%, 0 100%);
  }
  .social-banner--handle {
    left: 72px; top: 98px; width: 269px; padding-left: 38px;
    clip-path: polygon(0 0, 100% 0, 100% 100%, 0 100%, 8% 50%);
  }
  .social-dot {
    width: 26px; height: 26px; border-radius: 50%;
    background: var(--banner-ink); flex: none;
  }
  .portrait {
    position: absolute; left: 40px; top: 160px; width: 301px; height: 420px;
    background: linear-gradient(160deg, var(--photo-light) 0%, #9a9a94 45%, var(--photo-dark) 100%);
  }
</style>
</head>
<body>
<main class="canvas">
  <section class="card card--front" aria-label="Card front">
    <div class="monogram-seal" aria-hidden="true"></div>
    <h1 class="name-heading">Marlow Peskin</h1>
    <ul class="roles">
      <li class="role"><span class="role__fold"></span><span class="role__band"></span><span class="role__label">Bandleader</span></li>
      <li class="role"><span class="role__fold"></span><span class="role__band"></span><span class="role__label">Guitarist</span></li>
      <li class="role"><span class="role__fold"></span><span class="role__band"></span><span class="role__label">Vocalist</span></li>
      <li class="role"><span class="role__fold"></span><span class="role__band"></span><span class="role__label">Songwriter</span></li>
    </ul>
    <footer class="contact-bar">
      <span>marlowpeskin.com • marlow@marlowpeskin.com</span>
      <span>ph.: 646-555-0187</span>
    </footer>
  </section>

  <section class="card card--back" aria-label="Card back">
    <div class="portrait" role="img" aria-label="Black and white photo of the bandleader tipping a straw boater hat, wearing a dark striped blazer"></div>
    <div class="social-banner social-banner--site">
      <span class="social-dot" aria-hidden="true"></span>
      <span>marlowpeskin.com</span>
    </div>
    <div class="social-banner social-banner--handle">
      <span class="social-dot" aria-hidden="true"></span>
      <span>marlowpeskin</span>
    </div>
  </section>
</main>
</body>
</html>
```